Fine Dining Restaurant needs Harlow Stakes Day Flyer

We need a flyer to promote Harlow Stakes Day at our restaurant in Port Douglas, QLD.
Details:
6th November 2018
It's a ticketed event, including a fine-dining 4 course lunch, with 3 hour drinks package, to include sweeps & prizes.
Starts 11:30 - 14:30.
Ticket price: $160 with $5 from each ticket going to Birch & Bloom
Cash bar also available.
Address: 47 Lantern Street, Port Douglas
Contact: 0738152946 or bookings@corvinas.net.au
*Big screen TV's
*Sweeps
*Best Dressed prizes and more...
*Glass of sparkling wine on arrival
*Discount for tables of 8 or more...
Design: we'd like to see a really elegant design for the flyer, with the use of tropical florals, utilising whites and some burnt orange colours if suitable.
Size: To be printed on A4

```html
<!DOCTYPE html>
<html lang="en">
<head>
<meta charset="utf-8">
<title>Harlow Stakes Day Flyer</title>
<link rel="stylesheet" href="https://fonts.googleapis.com/css2?family=Great+Vibes&family=Oswald:wght@500;600&family=Montserrat:wght@500;600;800&display=swap">
<style>
  :root {
    --page-bg: #5f5f5f;
    --paper: #f7f7f6;
    --band: #efefee;
    --ink: #1c1c1c;
    --night: #080808;
    --burnt: #c4561b;
    --burnt-light: #e86a3c;
    --leaf: #3e8a46;
    --leaf-dark: #2f6b3a;
    --mint: #5ccfa4;
    --rule: #d79a72;
  }
  * { box-sizing: border-box; margin: 0; padding: 0; }
  html, body { width: 1200px; height: 1200px; overflow: hidden; }
  body { background: var(--page-bg); font-family: 'Montserrat', sans-serif; color: var(--ink); }

  .flyer {
    position: absolute; left: 195px; top: 27px;
    width: 810px; height: 1146px;
    background: var(--paper); overflow: hidden;
  }
  .frame-top {
    position: absolute; left: 250px; top: 24px; width: 536px; height: 270px;
    border-top: 1px solid var(--rule); border-right: 1px solid var(--rule);
  }
  .frame-bottom {
    position: absolute; left: 28px; top: 614px; width: 758px; height: 644px; max-height: 506px;
    border: 1px solid var(--rule); border-top: none;
  }

  .florals { position: absolute; z-index: 3; }
  .florals-top { left: 0; top: 0; width: 240px; height: 330px;
    background: radial-gradient(circle at 30% 35%, #b4603a 0 18%, #3f8550 19% 55%, rgba(63,133,80,0) 72%);
    border-bottom-right-radius: 60% 40%; }
  .florals-bottom { right: 0; bottom: 0; width: 330px; height: 170px;
    background: radial-gradient(circle at 40% 65%, #b4603a 0 16%, #3f8550 17% 52%, rgba(63,133,80,0) 72%);
    border-top-left-radius: 60% 50%; }

  .title { position: absolute; right: 40px; top: 28px; text-align: right; font-family: 'Great Vibes', cursive; line-height: 1; }
  .title-main { display: block; font-size: 140px; color: var(--burnt); }
  .title-sub { display: block; font-size: 112px; color: var(--leaf); margin-top: -18px; margin-right: 10px; }

  .date-band {
    position: absolute; left: 0; top: 283px; width: 810px; height: 331px; background: var(--night);
  }
  .venue-photo {
    position: absolute; right: 0; top: 0; width: 460px; height: 331px;
    background: linear-gradient(90deg, var(--night) 0%, #3b2a1c 22%, #6b4a2c 50%, #b65c33 80%, #d2773f 100%);
  }
  .date-block { position: absolute; left: 50px; top: 30px; color: #fff; z-index: 2; }
  .date-day {
    font-family: 'Montserrat', sans-serif; font-weight: 800; font-size: 170px; line-height: 1;
    letter-spacing: -4px;
    background: linear-gradient(180deg, #f47e54, #e2552b);
    -webkit-background-clip: text; background-clip: text; color: transparent;
  }
  .date-month { font-family: 'Oswald', sans-serif; font-weight: 600; font-size: 62px; line-height: 1; margin-top: 6px; letter-spacing: -1px; }
  .date-time { font-size: 25px; font-weight: 500; margin-top: 14px; margin-left: 44px; word-spacing: 6px; }

  .intro-band {
    position: absolute; left: 0; top: 614px; width: 810px; height: 136px;
    background: var(--band); text-align: center; padding-top: 22px;
  }
  .intro-script { font-family: 'Great Vibes', cursive; font-size: 38px; color: var(--leaf); line-height: 1.1; }
  .intro-text { font-weight: 600; font-size: 19px; line-height: 1.35; margin-top: 8px; }

  .details { position: absolute; left: 60px; top: 784px; width: 380px; }
  .label { font-family: 'Oswald', sans-serif; font-weight: 500; color: var(--burnt); font-size: 19px; }
  .ticket-row { display: flex; align-items: center; gap: 20px; margin-top: 18px; }
  .ticket-note { font-size: 15px; line-height: 1.3; width: 190px; }
  .ticket-note strong { color: var(--leaf); font-size: 18px; font-weight: 800; }
  .ticket-note .cash { color: var(--burnt); font-size: 13.5px; display: block; }
  .info-line { font-size: 15px; margin-top: 14px; line-height: 1.3; }
  .info-line + .info-line { margin-top: 10px; }

  .divider { position: absolute; left: 447px; top: 784px; width: 1px; height: 180px; background: #cfcfcf; }

  .perks { position: absolute; left: 470px; top: 796px; list-style: none; }
  .perks li { display: flex; align-items: center; gap: 12px; font-family: 'Oswald', sans-serif; font-weight: 500; font-size: 19px; color: var(--burnt); height: 33px; letter-spacing: -0.3px; }

  .brand { position: absolute; left: 60px; top: 1040px; font-family: 'Oswald', sans-serif; font-weight: 600; font-size: 36px; color: var(--ink); letter-spacing: -0.5px; }
</style>
</head>
<body>
<main class="flyer">
  <div class="frame-top"></div>
  <div class="frame-bottom"></div>

  <div class="florals florals-top" role="img" aria-label="Tropical florals: hibiscus, frangipani and palm leaves"></div>

  <h1 class="title">
    <span class="title-main">Harlow Stakes</span>
    <span class="title-sub">day</span>
  </h1>

  <section class="date-band">
    <div class="venue-photo" role="img" aria-label="Restaurant courtyard at dusk with pergola, lanterns and orange lounge seating"></div>
    <div class="date-block">
      <div class="date-day">6th</div>
      <div class="date-month">NOVEMBER 2018</div>
      <div class="date-time">Starts 11:30 - 14:30</div>
    </div>
  </section>

  <section class="intro-band">
    <p class="intro-script">It's a ticketed event, including a</p>
    <p class="intro-text">Fine-dining 4 course lunch, with 3 hour drinks package,<br>to include sweeps &amp; prizes.</p>
  </section>

  <section class="details">
    <div class="label">Ticket price:</div>
    <div class="ticket-row">
      <svg class="ticket" width="150" height="76" viewBox="0 0 150 76" aria-label="Ticket $160 + 5">
        <path d="M0 8 L6 0 L144 0 L150 8 L144 16 L150 24 L144 32 L150 40 L144 48 L150 56 L144 64 L150 72 L144 76 L6 76 L0 68 L6 60 L0 52 L6 44 L0 36 L6 28 L0 20 L6 12 Z" fill="var(--mint)"/>
        <rect x="22" y="7" width="106" height="62" fill="none" stroke="#2c6b55" stroke-width="1.5"/>
        <text x="75" y="46" text-anchor="middle" font-family="Oswald, sans-serif" font-weight="600" font-size="22" fill="#1c1c1c">$160+5</text>
      </svg>
      <p class="ticket-note">$160 with <strong>$5</strong> from each ticket going to Birch &amp; Bloom <span class="cash">Cash bar also available.</span></p>
    </div>
    <p class="info-line"><span class="label">Address:</span> 47 Lantern Street, Port Douglas</p>
    <p class="info-line"><span class="label">Contact:</span> 0738152946 or<br>bookings@corvinas.net.au</p>
  </section>

  <div class="divider"></div>

  <ul class="perks">
    <li><svg width="18" height="18" viewBox="0 0 18 18"><rect x="1" y="3" width="14" height="14" rx="3" fill="none" stroke="var(--leaf)" stroke-width="2"/><path d="M5 9 L8 12 L17 2" fill="none" stroke="var(--leaf)" stroke-width="2.4"/></svg>Big screen TV's</li>
    <li><svg width="18" height="18" viewBox="0 0 18 18"><rect x="1" y="3" width="14" height="14" rx="3" fill="none" stroke="var(--leaf)" stroke-width="2"/><path d="M5 9 L8 12 L17 2" fill="none" stroke="var(--leaf)" stroke-width="2.4"/></svg>Sweeps</li>
    <li><svg width="18" height="18" viewBox="0 0 18 18"><rect x="1" y="3" width="14" height="14" rx="3" fill="none" stroke="var(--leaf)" stroke-width="2"/><path d="M5 9 L8 12 L17 2" fill="none" stroke="var(--leaf)" stroke-width="2.4"/></svg>Best Dressed prizes and more...</li>
    <li><svg width="18" height="18" viewBox="0 0 18 18"><rect x="1" y="3" width="14" height="14" rx="3" fill="none" stroke="var(--leaf)" stroke-width="2"/><path d="M5 9 L8 12 L17 2" fill="none" stroke="var(--leaf)" stroke-width="2.4"/></svg>Glass of sparkling wine on arrival</li>
    <li><svg width="18" height="18" viewBox="0 0 18 18"><rect x="1" y="3" width="14" height="14" rx="3" fill="none" stroke="var(--leaf)" stroke-width="2"/><path d="M5 9 L8 12 L17 2" fill="none" stroke="var(--leaf)" stroke-width="2.4"/></svg>Discount for tables of 8 or more...</li>
  </ul>

  <div class="brand">CORVINA'S</div>

  <div class="florals florals-bottom" role="img" aria-label="Tropical florals: hibiscus, frangipani and leaves"></div>
</main>
</body>
</html>
```